GraniteLoop. Customer needs to know about us, what services we provide & contact us

We are a waste tire recycling company. Our primary focus is on providing a sustainable and cost effective service focusing on: Waste Tire Management, Hassle Free Scheduling for Tire Collection, Mobile Shredding & Special site cleanup services. GraniteLoop will be producing TDF, Clean Tire Wire & further materials.
Please look at https://quorvalwheel.example
Please look at https://bandimacorp.example

This is the look and feel of what we want

I have attached a word document with our website info.

Target Market(s)

Tire Install Companies. Such as paltonhaul.example. TDF Purchasers such as kevrofuel.example.

Industry/Entity Type

Waste Tire Recycling

Coding

Coded - Design and coding required

Number of Pages Required

3 page

Font styles to use
Other font styles liked:
• Look at our logo

Requirements
Must have
• We need a 3 page setup for About Us, Services & Contact Us. Contact us should be a form them can fill out and submit to us Images that are related to waste tire recycling. Clean, modern, innovative.
Nice to have
• The color and feel of the website should work with our logo that we did with artmarketly
Should not have
• Anything progressive, political or "woke"

```html
<!DOCTYPE html>
<html lang="en">
<head>
<meta charset="utf-8">
<title>GraniteLoop – Waste Tire Recycling</title>
<link href="https://fonts.googleapis.com/css2?family=Open+Sans:wght@400;600;700;800&family=Roboto:wght@400;500;700&display=swap" rel="stylesheet">
<style>
:root{
  --green:#0f8a3c;
  --green-dark:#0b7030;
  --ink:#222;
  --body:#6b6b6b;
  --line:#cfcfcf;
  --ghost:#ececec;
  --black:#060606;
  --white:#fff;
}
*{box-sizing:border-box;margin:0;padding:0}
html,body{width:1200px;height:3033px;overflow:hidden;background:var(--white)}
body{position:relative;font-family:"Roboto",sans-serif;color:var(--ink)}
.abs{position:absolute}
.topbar{left:0;top:0;width:1200px;height:4px;background:var(--green)}
.brand{left:110px;top:28px;display:flex;align-items:center;gap:12px;font-family:"Open Sans",sans-serif;font-weight:800;font-size:40px;color:var(--green);letter-spacing:-.5px}
.brand .dot{width:40px;height:40px;border-radius:50%;background:var(--green)}
.contact-line{right:110px;top:30px;font-size:15px;font-weight:500;color:#333;display:flex;gap:22px;align-items:center}
.contact-line span{display:flex;align-items:center;gap:7px}
.contact-line .sep{width:1px;height:24px;background:#bbb}
.nav{left:521px;top:74px;display:flex;gap:31px;font-size:15.5px;font-weight:500;color:#333}
.nav .active{color:var(--green);border-bottom:3px solid var(--green);padding-bottom:2px}
.socials{left:916px;top:67px;display:flex;gap:8px}
.socials i{display:block;width:38px;height:38px;border:1.5px solid #222;border-radius:50%}
.hero{left:0;top:118px;width:1200px;height:626px;background:linear-gradient(180deg,#55565a 0%,#3b3a37 35%,#2a2926 70%,#4a4843 100%)}
.hero-title{left:0;top:336px;width:1200px;text-align:center;font-family:"Open Sans",sans-serif;font-weight:800;font-size:64px;color:var(--green)}
.hero-sub{left:0;top:415px;width:1200px;text-align:center;font-family:"Open Sans",sans-serif;font-size:35px;color:var(--white);letter-spacing:.5px}
.btn{display:flex;align-items:center;justify-content:center;gap:7px;background:var(--green);color:var(--white);font-family:"Roboto",sans-serif;font-weight:700;border-radius:30px}
.hero-btn{left:495px;top:480px;width:210px;height:53px;font-size:16.5px}
.dots{left:558px;top:644px;display:flex;gap:9px}
.dots i{width:15px;height:15px;border-radius:50%;background:var(--white)}
.dots i.on{background:transparent;border:2px solid var(--green)}
.notch{left:562px;top:718px}
.ghost{font-family:"Open Sans",sans-serif;font-weight:800;color:var(--ghost);text-align:center}
.heading{font-family:"Open Sans",sans-serif;font-weight:800;color:var(--green);text-align:center}
.svc-ghost{left:0;top:790px;width:1200px;font-size:96px}
.svc-head{left:0;top:812px;width:1200px;font-size:64px}
.cards{left:112px;top:928px;width:976px;height:385px;display:flex}
.card{flex:1;position:relative;color:var(--white)}
.card p{position:absolute;left:0;right:0;bottom:28px;text-align:center;font-family:"Open Sans",sans-serif;font-weight:700;font-size:15px;line-height:26px}
.c1{background:linear-gradient(180deg,#9fb4c8 0%,#5e656b 40%,#26282a 100%)}
.c2{background:linear-gradient(160deg,#3a3c3f 0%,#6a7078 55%,#2a2c30 100%)}
.c3{background:linear-gradient(120deg,#4a4c4f 0%,#9a9ea3 45%,#c46a3a 100%)}
.about-img{left:0;top:1399px;width:598px;height:578px;background:linear-gradient(180deg,#d9dcd6 0%,#6c6f6c 30%,#2e2f2e 80%,#444 100%)}
.about-head{left:643px;top:1393px;font-size:68px;text-align:left}
.about-text{left:641px;top:1480px;width:447px;font-size:15px;line-height:25.8px;color:var(--body);text-align:justify}
.about-text p+p{margin-top:25.8px}
.about-btn{left:643px;top:1889px;width:194px;height:53px;font-size:17px}
.about-ghost{left:1098px;top:1465px;width:80px;height:450px;font-size:84px;writing-mode:vertical-rl;line-height:80px;text-align:left}
.git-ghost{left:0;top:2024px;width:1200px;font-size:96px}
.git-head{left:0;top:2046px;width:1200px;font-size:64px}
.info{top:2166px;width:240px;text-align:center;font-size:13.5px;line-height:21px;color:#333}
.info .ic{width:64px;height:64px;margin:0 auto 10px;border:2px solid var(--green);border-radius:50%;display:flex;align-items:center;justify-content:center}
.info b{display:block;font-weight:500;font-size:15px;margin-bottom:1px}
.field{height:40px;border-bottom:1px solid var(--line);font-size:14px;color:#888;padding:4px 11px}
.submit{left:518px;top:2524px;width:163px;height:45px;font-size:15.5px}
.footer{left:0;top:2654px;width:1200px;height:379px;background:linear-gradient(180deg,var(--black) 0%,var(--black) 55%,#1c1c1c 80%,#2a2a2a 100%)}
.fcol{top:2720px;color:var(--white);font-size:14.5px}
.fcol h4{font-size:14.5px;font-weight:700;text-decoration:underline;margin-bottom:20px}
.fcol li{list-style:none;height:37px;display:flex;align-items:flex-start;gap:14px}
.fcol li span.ar{font-weight:700;font-size:13px}
.fsoc{display:flex;gap:8px;margin-bottom:20px}
.fsoc i{width:32px;height:32px;border:1.5px solid var(--white);border-radius:50%}
.news{display:flex;width:310px;height:48px;background:var(--white);border:1px solid #ddd}
.news span{flex:1;color:#777;font-size:14px;padding:15px 16px}
.news b{width:48px;background:var(--green);display:flex;align-items:center;justify-content:center}
.copy{left:0;top:2994px;width:1200px;text-align:center;color:var(--white);font-size:14.5px}
</style>
</head>
<body>
<div class="abs topbar"></div>
<header>
  <div class="abs brand"><span class="dot"></span>GraniteLoop</div>
  <div class="abs contact-line">
    <span><svg width="15" height="12" viewBox="0 0 15 12"><rect x="0.5" y="0.5" width="14" height="11" fill="#333"/><path d="M1 1l6.5 5L14 1" stroke="#fff" fill="none"/></svg>Mail us : info@graniteloop.example</span>
    <i class="sep"></i>
    <span><svg width="13" height="13" viewBox="0 0 24 24"><path fill="#333" d="M6.6 10.8a15 15 0 006.6 6.6l2.2-2.2a1 1 0 011-.25 11 11 0 003.6.6 1 1 0 011 1V20a1 1 0 01-1 1A17 17 0 013 4a1 1 0 011-1h3.5a1 1 0 011 1 11 11 0 00.6 3.6 1 1 0 01-.25 1z"/></svg>Call us Today : +1 555 010 0188</span>
  </div>
  <nav class="abs nav"><span class="active">Home</span><span>About Us</span><span>Services</span><span>Contact Us</span></nav>
  <div class="abs socials"><i></i><i></i><i></i><i></i></div>
</header>

<section>
  <div class="abs hero" role="img" aria-label="Yard piled high with scrap tires and a loader"></div>
  <h1 class="abs hero-title">GraniteLoop</h1>
  <p class="abs hero-sub">We are a waste tire recycling company</p>
  <div class="abs btn hero-btn">GET STARTED <svg width="16" height="16" viewBox="0 0 16 16"><circle cx="8" cy="8" r="8" fill="#fff"/><path d="M6.5 4.5L10 8l-3.5 3.5" stroke="#0f8a3c" stroke-width="2" fill="none"/></svg></div>
  <div class="abs dots"><i></i><i class="on"></i><i></i><i></i></div>
  <svg class="abs notch" width="76" height="27" viewBox="0 0 76 27"><path d="M0 27L38 0l38 27z" fill="#fff"/><path d="M33 15l5 4 5-4M33 19l5 4 5-4" stroke="#0f8a3c" stroke-width="1.6" fill="none"/></svg>
</section>

<section>
  <div class="abs ghost svc-ghost">Our Services</div>
  <h2 class="abs heading svc-head">Our Services</h2>
  <div class="abs cards">
    <div class="card c1" role="img" aria-label="Heap of used tires under a blue sky"><p>Waste Tire Management</p></div>
    <div class="card c2" role="img" aria-label="Worker carrying a tire for collection"><p>Hassle Free Scheduling for<br>Tire Collection</p></div>
    <div class="card c3" role="img" aria-label="Wheel being removed with an impact wrench"><p>Mobile Shredding &amp; Special<br>site cleanup services.</p></div>
  </div>
</section>

<section>
  <div class="abs about-img" role="img" aria-label="Worker holding a tire in front of a tire pile"></div>
  <div class="abs ghost about-ghost">About us</div>
  <h2 class="abs heading about-head">About us</h2>
  <div class="abs about-text">
    <p>Lorem ipsum dolor sit amet, consectetur adipiscing elit, sed do eius mod tempor incididunt ut labore et dolore magna aliqua. Ut enim ad minim veniam, quis nostrud exercitation ullamco laboris nisi ut aliq uip ex ea commodo consequat. Duis aute irure dolor in reprehenderit in voluptate velit esse cillum dolore eu fugiat nulla pariatur. Excepteur sint occaecat cupidatat non proident, sunt in culpa qui officia deseru nt mollit anim id est laborum.</p>
    <p>Lorem ipsum dolor sit amet, consectetur adipiscing elit, sed do eius mod tempor incididunt ut labore et dolore magna aliqua. Ut enim ad minim veniam, quis nostrud exercitation ullamco laboris nisi ut aliq uip ex ea commodo consequat. Duis aute irure dolor in reprehenderit in voluptate velit esse cillum dolore eu fugiat nulla pariatur. Excepteur sint occaecat cupidatat non proident, sunt in culpa qui officia deserunt mollit anim id est laborum.</p>
  </div>
  <div class="abs btn about-btn">LEARN MORE <svg width="16" height="16" viewBox="0 0 16 16"><circle cx="8" cy="8" r="8" fill="#fff"/><path d="M6.5 4.5L10 8l-3.5 3.5" stroke="#0f8a3c" stroke-width="2" fill="none"/></svg></div>
</section>

<section>
  <div class="abs ghost git-ghost">Get in Touch</div>
  <h2 class="abs heading git-head">Get in Touch</h2>
  <div class="abs info" style="left:247px"><div class="ic"><svg width="18" height="24" viewBox="0 0 18 24"><path d="M9 0a9 9 0 00-9 9c0 7 9 15 9 15s9-8 9-15a9 9 0 00-9-9z" fill="#0f8a3c"/><circle cx="9" cy="9" r="3.3" fill="#fff"/></svg></div><b>ADDRESS :</b>123,Lorem ipsum dolor sit amet,<br>consectetur</div>
  <div class="abs info" style="left:487px"><div class="ic"><svg width="22" height="22" viewBox="0 0 24 24"><path fill="#0f8a3c" d="M6.6 10.8a15 15 0 006.6 6.6l2.2-2.2a1 1 0 011-.25 11 11 0 003.6.6 1 1 0 011 1V20a1 1 0 01-1 1A17 17 0 013 4a1 1 0 011-1h3.5a1 1 0 011 1 11 11 0 00.6 3.6 1 1 0 01-.25 1z"/></svg></div><b>PHONE :</b>+1 555 010 0188</div>
  <div class="abs info" style="left:727px"><div class="ic"><svg width="24" height="18" viewBox="0 0 24 18"><rect width="24" height="18" rx="2" fill="#0f8a3c"/><path d="M1 2l11 8 11-8" stroke="#fff" stroke-width="2" fill="none"/></svg></div><b>EMAIL :</b>info@graniteloop.example</div>
  <div class="abs field" style="left:203px;top:2325px;width:234px">Your name *</div>
  <div class="abs field" style="left:483px;top:2325px;width:234px">Phone *</div>
  <div class="abs field" style="left:763px;top:2325px;width:235px">Email address *</div>
  <div class="abs field" style="left:203px;top:2455px;width:795px">Message *</div>
  <div class="abs btn submit">SUBMIT NOW</div>
</section>

<footer>
  <div class="abs footer" role="img" aria-label="Dark close-up of tire treads"></div>
  <div class="abs fcol" style="left:110px"><h4>QUICK LINKS</h4><ul>
    <li><span class="ar">»</span>Home</li><li><span class="ar">»</span>About me</li><li><span class="ar">»</span>Gallery</li><li><span class="ar">»</span>References</li><li><span class="ar">»</span>Latest Blog</li></ul></div>
  <div class="abs fcol" style="left:295px"><h4>OTHER LINKS</h4><ul>
    <li><span class="ar">»</span>Terms &amp; Conditions</li><li><span class="ar">»</span>Privacy Policy</li><li><span class="ar">»</span>Help Service</li><li><span class="ar">»</span>FAQ</li><li><span class="ar">»</span>Contact us</li></ul></div>
  <div class="abs fcol" style="left:527px;width:230px"><h4>FIND US ON</h4><ul>
    <li><svg width="10" height="14" viewBox="0 0 18 24"><path d="M9 0a9 9 0 00-9 9c0 7 9 15 9 15s9-8 9-15a9 9 0 00-9-9z" fill="#fff"/></svg><span style="margin-left:8px">201 , Lorem ipsum dolor sit</span></li>
    <li><span style="margin-left:31px">amet, consectetur</span></li>
    <li><svg width="12" height="12" viewBox="0 0 24 24"><path fill="#fff" d="M6.6 10.8a15 15 0 006.6 6.6l2.2-2.2a1 1 0 011-.25 11 11 0 003.6.6 1 1 0 011 1V20a1 1 0 01-1 1A17 17 0 013 4a1 1 0 011-1h3.5a1 1 0 011 1 11 11 0 00.6 3.6 1 1 0 01-.25 1z"/></svg><span style="margin-left:6px">+1 555 010 018</span></li>
    <li><svg width="13" height="10" viewBox="0 0 24 18"><rect x="1" y="1" width="22" height="16" fill="none" stroke="#fff" stroke-width="2"/><path d="M1 2l11 8 11-8" stroke="#fff" stroke-width="2" fill="none"/></svg><span style="margin-left:5px">info@graniteloop.example</span></li></ul></div>
  <div class="abs fcol" style="left:779px"><h4>CONNECTED US ON</h4>
    <div class="fsoc"><i></i><i></i><i></i><i></i><i></i></div>
    <h4>SUBSCRIBE TO OUR NEWSLETTER</h4>
    <div class="news"><span>Email Address</span><b><svg width="20" height="20" viewBox="0 0 20 20"><path d="M19 1L1 8l7 3 3 7z" fill="#fff"/></svg></b></div>
  </div>
  <div class="abs copy">© 2022 GraniteLoop. All Rights Reserved</div>
</footer>
</body>
</html>
```